Tyre Company Stationary
Stationary design
Simple
Colin Ruddock
Managing Director
Marlow's Building
582b/F/3 Oleander Road
Lusaka
Zambia
colinruddock@brenholdia.com
www.brenholdia.com
This is my AI Logo

```html
<!DOCTYPE html>
<html lang="en">
<head>
<meta charset="utf-8">
<title>Brenholdia Stationery</title>
<link href="https://fonts.googleapis.com/css2?family=Exo+2:wght@400;700&display=swap" rel="stylesheet">
<style>
  :root {
    --bg: #2a2623;
    --paper: #ffffff;
    --paper-shade: #e9e9e9;
    --orange: #f39200;
    --ink: #222222;
    --muted: #9a9a9a;
    --card-dark: #1c1c1c;
  }
  * { box-sizing: border-box; margin: 0; padding: 0; }
  html, body { width: 1200px; height: 266px; overflow: hidden; }
  body { background: var(--bg); font-family: "Exo 2", sans-serif; position: relative; color: var(--ink); }
  .item { position: absolute; background: var(--paper); overflow: hidden; box-shadow: 0 2px 6px rgba(0,0,0,.5); }
  .brand { display: flex; align-items: center; gap: 3px; font-weight: 700; color: var(--ink); white-space: nowrap; }
  .brand .dot { border-radius: 50%; background: var(--orange); flex: none; }
  .brand.on-dark { color: var(--paper); }
  .faint-circle { position: absolute; border-radius: 50%; border: 6px solid rgba(0,0,0,.07); }
  .small { font-size: 4px; line-height: 5.5px; color: var(--muted); }

  /* envelopes */
  .envelope-back { left: 24px; top: 24px; width: 116px; height: 52px; }
  .envelope-front { left: 24px; top: 80px; width: 120px; height: 48px; }
  .envelope-small { left: 24px; top: 134px; width: 116px; height: 56px; }

  /* letterheads */
  .letterhead { top: 70px; width: 108px; height: 142px; }
  .letterhead.one { left: 156px; }
  .letterhead.two { left: 282px; }
  .letter-body { position: absolute; left: 10px; top: 40px; width: 88px; font-size: 4px; line-height: 6px; color: var(--muted); }

  /* main logo */
  .main-logo { left: 540px; top: 30px; position: absolute; }

  /* business cards */
  .card { width: 96px; height: 48px; }
  .card.dark { left: 548px; top: 86px; background: var(--card-dark); }
  .card.light { left: 548px; top: 142px; }
  .card.mini { left: 440px; width: 84px; height: 42px; }

  /* folders */
  .folder-open { left: 758px; top: 76px; width: 206px; height: 160px; background: none; box-shadow: none; display: flex; }
  .folder-open .panel { position: relative; width: 103px; height: 160px; overflow: hidden; box-shadow: 0 2px 6px rgba(0,0,0,.5); }
  .panel.white { background: var(--paper); }
  .panel.orange { background: var(--orange); }
  .folder-pocket { left: 980px; top: 76px; width: 200px; height: 160px; background: none; box-shadow: none; display: flex; }
  .folder-pocket .panel { position: relative; width: 100px; height: 160px; overflow: hidden; box-shadow: 0 2px 6px rgba(0,0,0,.5); }
  .pocket { position: absolute; left: 0; bottom: 0; width: 100%; height: 62px; background: var(--paper); }
  .pocket-card { position: absolute; left: 14px; top: 62px; width: 60px; height: 30px; background: var(--paper); border: 1px solid var(--paper-shade); }
</style>
</head>
<body>

<!-- envelope back with orange flap -->
<div class="item envelope-back">
  <svg width="116" height="52" viewBox="0 0 116 52">
    <polygon points="0,0 116,0 58,24" fill="var(--orange)"/>
    <line x1="0" y1="52" x2="58" y2="26" stroke="var(--paper-shade)"/>
    <line x1="116" y1="52" x2="58" y2="26" stroke="var(--paper-shade)"/>
  </svg>
</div>

<!-- envelope front -->
<div class="item envelope-front">
  <div class="brand" style="position:absolute;left:8px;top:8px;font-size:7px;"><span class="dot" style="width:6px;height:6px"></span>brenholdia</div>
  <div class="small" style="position:absolute;left:8px;top:18px;">Marlow's Building<br>582b/F/3 Oleander Road</div>
  <div style="position:absolute;left:0;bottom:6px;width:100%;height:3px;background:var(--orange)"></div>
</div>

<!-- small envelope -->
<div class="item envelope-small">
  <div class="brand" style="position:absolute;left:8px;top:8px;font-size:7px;"><span class="dot" style="width:6px;height:6px"></span>brenholdia</div>
  <div style="position:absolute;left:0;bottom:0;width:100%;height:10px;background:var(--orange)"></div>
</div>

<!-- letterhead one -->
<div class="item letterhead one">
  <div class="faint-circle" style="left:24px;top:40px;width:60px;height:60px"></div>
  <div class="brand" style="position:absolute;left:10px;top:10px;font-size:7px;"><span class="dot" style="width:6px;height:6px"></span>brenholdia</div>
  <p class="letter-body">Thank you for choosing our tyres and service.</p>
  <svg style="position:absolute;left:0;bottom:0" width="108" height="24" viewBox="0 0 108 24">
    <path d="M0 10 Q54 0 108 14 L108 24 L0 24 Z" fill="var(--orange)"/>
  </svg>
</div>

<!-- letterhead two -->
<div class="item letterhead two">
  <div class="faint-circle" style="left:24px;top:40px;width:60px;height:60px"></div>
  <div class="brand" style="position:absolute;left:10px;top:10px;font-size:7px;"><span class="dot" style="width:6px;height:6px"></span>brenholdia</div>
  <p class="letter-body">Quality tyres fitted fast, every single day.</p>
  <svg style="position:absolute;left:0;bottom:0" width="108" height="24" viewBox="0 0 108 24">
    <path d="M0 14 Q54 0 108 10 L108 24 L0 24 Z" fill="var(--orange)"/>
  </svg>
</div>

<!-- main logo -->
<div class="main-logo brand on-dark" style="font-size:15px;gap:6px;">
  <span class="dot" style="width:16px;height:16px"></span>brenholdia
</div>

<!-- small cards -->
<div class="item card mini" style="top:90px">
  <div class="brand" style="position:absolute;left:6px;top:15px;font-size:6px;"><span class="dot" style="width:5px;height:5px"></span>brenholdia</div>
</div>
<div class="item card mini" style="top:144px">
  <div class="small" style="position:absolute;left:6px;top:8px;"><b style="color:var(--ink)">Colin Ruddock</b><br>Managing Director<br>colinruddock@brenholdia.com</div>
</div>

<!-- business cards -->
<div class="item card dark">
  <div class="brand on-dark" style="position:absolute;left:8px;top:10px;font-size:7px;"><span class="dot" style="width:6px;height:6px"></span>brenholdia</div>
  <svg style="position:absolute;left:0;bottom:0" width="96" height="16" viewBox="0 0 96 16">
    <path d="M0 10 Q48 0 96 8 L96 16 L0 16 Z" fill="var(--orange)"/>
  </svg>
</div>
<div class="item card light">
  <div class="small" style="position:absolute;left:8px;top:6px;"><b style="color:var(--ink)">Colin Ruddock</b><br>Managing Director<br>Marlow's Building, 582b/F/3 Oleander Road<br>Lusaka, Zambia<br>www.brenholdia.com</div>
  <div style="position:absolute;left:0;bottom:0;width:100%;height:4px;background:var(--orange)"></div>
</div>

<!-- open folder -->
<div class="item folder-open">
  <div class="panel white">
    <div class="faint-circle" style="left:22px;top:40px;width:60px;height:60px"></div>
    <div style="position:absolute;left:0;top:0;width:100%;height:10px;background:var(--orange)"></div>
  </div>
  <div class="panel orange">
    <div class="faint-circle" style="left:22px;top:40px;width:60px;height:60px;border-color:rgba(255,255,255,.18)"></div>
  </div>
</div>

<!-- pocket folder -->
<div class="item folder-pocket">
  <div class="panel white">
    <div class="faint-circle" style="left:20px;top:30px;width:60px;height:60px"></div>
  </div>
  <div class="panel orange">
    <div class="pocket"></div>
    <div class="pocket-card">
      <div class="brand" style="position:absolute;left:4px;top:10px;font-size:5px;"><span class="dot" style="width:4px;height:4px"></span>brenholdia</div>
    </div>
  </div>
</div>

</body>
</html>
```